A web site for my wholesale/retail cleaning supplies company

I need a website that can accept payment from retail and wholesale customers. A good example is fresh meadow goods website. My company name is bright leaf northern. We will be selling sanitizers, all purpose cleaners, soaps and things of the such. All natural stuff.
Updates

Please focus on hand sanitizer as well. That will actually be my first product. Contact number 4035550187 email brightleafnorthern@mailbox-example.com for contact Facebook is www.socialpage-example.com/brightleafnorthern

Coding

Coded - Design and coding required

Number of Pages Required

1 page

Requirements
Must have
• Wholesale
Retail
Both in seperate sections.
Instagram brightleafnorthern
Facebook www.socialpage-example.com/brightleafnorthern
Email brightleafnorthern@mailbox-example.com
Number 4035550187

About us

Bright Leaf Northern is %100 canada based. We believe in building local communities and business together with locally sourced ingredients. As well as making safe alternatives to the harsh chemicals we are exposed to every day during simple tasks. Many cleaning supplies or household products can irritate the eyes or throat, or cause headaches and other health problems, including cancer. Some products release dangerous chemicals, including volatile organic compounds (VOC's). We find this to be not only uneccisary but widely dangerous. Join the "Spread" as we naturally cruise through canada creating healthier families everywhere.

```html
<!DOCTYPE html>
<html lang="en">
<head>
<meta charset="utf-8">
<title>Bright Leaf Northern – Natural Cleaning Supplies</title>
<link href="https://fonts.googleapis.com/css2?family=Montserrat:wght@500;600;700;800&family=Open+Sans:wght@400;600;700&display=swap" rel="stylesheet">
<style>
:root{
  --green:#6ab43e;
  --green-dark:#57992f;
  --blue:#2ba4dc;
  --blue-dark:#1f88bd;
  --ink:#2b2b2b;
  --muted:#777;
  --line:#dedede;
  --blog-bg:#eef8e3;
  --footer:#232323;
  --footer-bottom:#151515;
  --star:#f5a623;
  --white:#fff;
}
*{box-sizing:border-box;margin:0;padding:0}
html,body{width:1200px;height:3504px;overflow:hidden}
body{font-family:"Open Sans",sans-serif;color:var(--ink);background:var(--white);font-size:13px}
h1,h2,h3,h4,.heading{font-family:"Montserrat",sans-serif}
.container{width:940px;margin:0 auto}
.wide{width:1136px;margin:0 auto}

/* top bar */
.topbar{height:28px;background:var(--green);color:var(--white);font-size:11px}
.topbar .wide{display:flex;justify-content:space-between;align-items:center;height:28px}
.topbar span{margin-right:22px}
.topbar .right span{margin:0 0 0 22px}

/* header */
.header{height:140px}
.header .wide{display:flex;align-items:center;height:140px}
.brand{width:220px;display:flex;align-items:center;gap:10px}
.brand-dot{width:18px;height:18px;border-radius:50%;background:var(--green);flex:none}
.brand-name{font-family:"Montserrat",sans-serif;font-weight:700;font-size:19px;line-height:1.15;color:var(--blue);text-transform:uppercase}
.search{margin-left:108px;width:480px;height:34px;display:flex;border:1px solid var(--line)}
.search input{flex:1;border:0;padding:0 12px;font-size:12px;font-family:inherit;color:var(--muted)}
.search .cat{width:130px;border-left:1px solid var(--line);display:flex;align-items:center;justify-content:space-between;padding:0 10px;font-size:12px;color:var(--muted)}
.search .go{width:40px;background:var(--green);display:flex;align-items:center;justify-content:center}
.cart{margin-left:auto;display:flex;align-items:center;gap:10px;margin-right:48px}
.cart .ico{width:40px;height:40px;border:1px solid var(--line);border-radius:50%;display:flex;align-items:center;justify-content:center}
.cart b{display:block;font-size:11px;font-family:"Montserrat",sans-serif}
.cart small{font-size:11px;color:var(--muted)}

/* nav */
.nav{height:32px;background:var(--blue)}
.nav ul{list-style:none;display:flex;height:32px}
.nav li{padding:0 22px;line-height:32px;color:var(--white);font-family:"Montserrat",sans-serif;font-weight:700;font-size:11px}
.nav li.active{background:var(--green)}

/* hero */
.hero{position:relative;height:392px;background:linear-gradient(90deg,#8d9499 0%,#b9bec2 40%,#d9dcde 70%,#c4c8cb 100%)}
.hero-copy{position:absolute;left:132px;top:92px;color:var(--white)}
.hero-copy h1{font-size:38px;font-weight:800;line-height:1.2;text-transform:uppercase}
.hero-copy p{font-size:22px;margin-top:6px}
.btn{display:inline-block;background:var(--green);color:var(--white);font-family:"Montserrat",sans-serif;font-weight:700;font-size:12px;text-transform:uppercase}
.hero .btn{margin-top:30px;padding:11px 22px}
.dots{position:absolute;left:50%;bottom:14px;transform:translateX(-50%);display:flex;gap:6px}
.dots i{width:22px;height:3px;background:rgba(255,255,255,.6)}
.dots i.on{background:var(--white)}

/* features */
.features{height:260px;padding-top:108px}
.features .container{display:flex;gap:20px}
.feature{width:300px;height:120px;border:1px solid var(--line);padding:14px 18px}
.feature-head{display:flex;align-items:center;justify-content:center;gap:12px;padding-bottom:12px;border-bottom:1px solid var(--line)}
.feature-head h3{font-size:14px;font-weight:700;text-transform:uppercase}
.feature p{font-size:11px;color:var(--muted);line-height:1.5;margin-top:10px}

/* section titles */
.section-title{text-align:center;font-weight:700;font-size:25px;line-height:40px}
.section-title.blue{color:var(--blue)}

/* collections */
.collections{height:400px;padding-top:32px}
.collection-grid{display:flex;gap:24px;margin-top:36px}
.collection{width:217px;text-align:center}
.collection .photo{height:220px}
.collection h4{margin-top:14px;font-size:12px;font-weight:700;text-transform:uppercase;line-height:20px}

/* benefits */
.benefits{height:188px;padding-top:50px}
.benefits .container{display:flex;justify-content:space-around;padding:0 40px}
.benefit{display:flex;align-items:center;gap:16px;height:96px}
.benefit .ring{width:76px;height:76px;border:2px solid var(--blue);border-radius:50%;display:flex;align-items:center;justify-content:center}
.benefit b{display:block;font-family:"Montserrat",sans-serif;font-size:20px;font-weight:800}
.benefit span{font-size:11px;text-transform:uppercase;color:var(--muted)}

/* products */
.products{height:1160px;padding-top:32px}
.product-grid{display:grid;grid-template-columns:repeat(4,217px);column-gap:24px;row-gap:84px;margin-top:56px}
.product .photo{height:252px}
.product h4{margin-top:16px;height:40px;font-family:"Open Sans",sans-serif;font-size:13px;font-weight:600;line-height:18px}
.product .price{margin-top:44px;font-size:13px;line-height:20px}
.stars{color:var(--star);font-size:12px;line-height:16px;letter-spacing:1px}
.product .btn{margin-top:14px;background:var(--green-dark);font-family:"Open Sans",sans-serif;font-weight:600;text-transform:none;font-size:11px;padding:0 10px;line-height:26px}

/* blog */
.blog{height:520px;padding-top:32px;background:var(--blog-bg);text-align:center}
.blog-grid{display:flex;gap:20px;margin-top:28px;text-align:left}
.post{width:300px}
.post .photo{height:180px;position:relative}
.date{position:absolute;left:0;bottom:0;width:48px;height:48px;background:var(--green);color:var(--white);text-align:center;font-family:"Montserrat",sans-serif;font-weight:700;font-size:18px;line-height:26px}
.date small{display:block;font-size:9px;line-height:12px}
.post h4{margin-top:14px;font-size:12px;font-weight:700;line-height:18px;text-transform:uppercase}
.post p{margin-top:8px;font-size:11px;line-height:16px;color:var(--muted)}
.blog .btn{margin-top:80px;background:#1c1c1c;padding:0 24px;line-height:30px;font-size:11px}

/* newsletter */
.newsletter{height:148px;display:flex;align-items:center}
.newsletter .container{display:flex;align-items:center;padding-left:82px}
.newsletter h3{font-size:17px;font-weight:700;text-transform:uppercase;width:380px}
.newsletter .field{width:288px;height:40px;border:1px solid var(--line);padding:0 14px;display:flex;align-items:center;color:var(--muted);font-size:12px}
.newsletter .submit{height:40px;width:100px;background:var(--blue);color:var(--white);font-family:"Montserrat",sans-serif;font-weight:700;font-size:12px;display:flex;align-items:center;justify-content:center;text-transform:uppercase}

/* footer */
.footer{height:204px;background:var(--footer);color:#cfcfcf;padding-top:40px}
.footer .container{display:flex}
.footer-col{width:240px}
.footer-col:last-child{width:220px}
.footer-col h5{font-family:"Montserrat",sans-serif;color:var(--white);font-size:12px;font-weight:700;text-transform:uppercase;margin-bottom:14px}
.footer-col li{list-style:none;font-size:11px;line-height:22px}
.footer-col li.contact{display:flex;gap:8px;align-items:center;white-space:nowrap}
.footer-bottom{height:32px;background:var(--footer-bottom);color:#9a9a9a;font-size:11px;text-align:center;line-height:32px}
</style>
</head>
<body>

<div class="topbar">
  <div class="wide">
    <div class="left"><span>Call Us : 4035550187</span><span>Mail Us : brightleafnorthern@mailbox-example.com</span></div>
    <div class="right"><span>CAD ▾</span><span>My Account</span></div>
  </div>
</div>

<header class="header">
  <div class="wide">
    <div class="brand"><span class="brand-dot"></span><span class="brand-name">Bright Leaf Northern</span></div>
    <div class="search">
      <input type="text" placeholder="Search">
      <div class="cat">All Categories <span>▾</span></div>
      <div class="go"><svg width="16" height="16" viewBox="0 0 16 16"><circle cx="6.5" cy="6.5" r="4.5" fill="none" stroke="#fff" stroke-width="2"/><path d="M10 10l4 4" stroke="#fff" stroke-width="2"/></svg></div>
    </div>
    <div class="cart">
      <div class="ico"><svg width="20" height="20" viewBox="0 0 20 20"><path d="M2 3h3l2 9h9l2-6H6" fill="none" stroke="#2b2b2b" stroke-width="1.6"/><circle cx="8" cy="16" r="1.5" fill="#2b2b2b"/><circle cx="15" cy="16" r="1.5" fill="#2b2b2b"/></svg></div>
      <div><b>MY CART</b><small>0 item - $0.00</small></div>
    </div>
  </div>
</header>

<nav class="nav">
  <ul class="container">
    <li class="active">HOME</li><li>ALL PRODUCTS</li><li>ABOUT US</li><li>STORE</li><li>FINDUS</li><li>BLOGS</li><li>CONTACT</li>
  </ul>
</nav>

<section class="hero" role="img" aria-label="Smiling cleaner holding a basket of cleaning bottles in a bright kitchen">
  <div class="hero-copy">
    <h1>We supply all<br>cleaning product</h1>
    <p>in Wholesale and retail Prices</p>
    <span class="btn">Shop Now</span>
  </div>
  <div class="dots"><i></i><i class="on"></i><i></i></div>
</section>

<section class="features">
  <div class="container">
    <div class="feature">
      <div class="feature-head">
        <svg width="30" height="20" viewBox="0 0 30 20"><rect x="1" y="3" width="17" height="11" fill="none" stroke="#6ab43e" stroke-width="1.6"/><path d="M18 7h6l4 4v3H18" fill="none" stroke="#6ab43e" stroke-width="1.6"/><circle cx="7" cy="16" r="2.5" fill="#fff" stroke="#6ab43e" stroke-width="1.6"/><circle cx="23" cy="16" r="2.5" fill="#fff" stroke="#6ab43e" stroke-width="1.6"/></svg>
        <h3>Free Shipping</h3>
      </div>
      <p>For Canadian orders over $50, shipping is free. It's our way of saying thanks.</p>
    </div>
    <div class="feature">
      <div class="feature-head"><h3>What we say</h3></div>
      <p>Join the conversation on our blog to know why our products are so natural.</p>
    </div>
    <div class="feature">
      <div class="feature-head">
        <svg width="26" height="20" viewBox="0 0 26 20"><circle cx="9" cy="6" r="4" fill="none" stroke="#6ab43e" stroke-width="1.6"/><path d="M2 19c0-5 3-7 7-7s7 2 7 7" fill="none" stroke="#6ab43e" stroke-width="1.6"/><path d="M20 6v8M16 10h8" stroke="#6ab43e" stroke-width="1.6"/></svg>
        <h3>Join mailing list</h3>
      </div>
      <p>Want to get latest offers, discounts and deals, join our mailing list.</p>
    </div>
  </div>
</section>

<section class="collections">
  <div class="container">
    <h2 class="section-title blue">Featured Collections</h2>
    <div class="collection-grid">
      <div class="collection"><div class="photo" role="img" aria-label="Colourful pocket hand sanitizer bottles" style="background:linear-gradient(135deg,#7fd0ec,#f08bb8 55%,#9fd46a)"></div><h4>Hand Sanitizers</h4></div>
      <div class="collection"><div class="photo" role="img" aria-label="Large bottles of cleaning solution" style="background:linear-gradient(135deg,#e6f1f8,#7cb5dc)"></div><h4>Cleaning Solutions</h4></div>
      <div class="collection"><div class="photo" role="img" aria-label="Stack of natural bath soaps" style="background:linear-gradient(135deg,#e9e2d4,#b7a68a)"></div><h4>Bath and Body Care</h4></div>
      <div class="collection"><div class="photo" role="img" aria-label="Oral care products on pink background" style="background:linear-gradient(135deg,#f8e3e4,#e8a9ae)"></div><h4>Oral Care</h4></div>
    </div>
  </div>
</section>

<section class="benefits">
  <div class="container">
    <div class="benefit">
      <div class="ring"><svg width="38" height="38" viewBox="0 0 38 38"><path d="M19 4l12 5v9c0 8-6 13-12 16C13 31 7 26 7 18V9z" fill="none" stroke="#6ab43e" stroke-width="2"/><path d="M13 19l4 4 8-8" fill="none" stroke="#2ba4dc" stroke-width="2"/></svg></div>
      <div><b>KILLS</b><span>Harmful Bacterias</span></div>
    </div>
    <div class="benefit">
      <div class="ring"><svg width="38" height="38" viewBox="0 0 38 38"><path d="M19 5c6 9 10 14 10 19a10 10 0 0 1-20 0c0-5 4-10 10-19z" fill="none" stroke="#6ab43e" stroke-width="2"/><path d="M14 25a5 5 0 0 0 5 5" fill="none" stroke="#2ba4dc" stroke-width="2"/></svg></div>
      <div><b>PURE</b><span>Essential Oils</span></div>
    </div>
    <div class="benefit">
      <div class="ring"><svg width="38" height="38" viewBox="0 0 38 38"><path d="M8 30C8 16 18 8 31 8c0 13-8 22-21 22z" fill="none" stroke="#6ab43e" stroke-width="2"/><path d="M8 30l14-14" stroke="#2ba4dc" stroke-width="2"/></svg></div>
      <div><b>100%</b><span>Natural &amp; Hygienic</span></div>
    </div>
  </div>
</section>

<section class="products">
  <div class="container">
    <h2 class="section-title">Top Selling Products</h2>
    <div class="product-grid">
      <div class="product"><div class="photo" role="img" aria-label="Bundle of wrapped sanitizer soap bars" style="background:linear-gradient(135deg,#f1ece4,#c9a77d)"></div><h4>20 Pack Hand Sanitizer</h4><div class="price">$ 25.00 CAD</div><div class="stars">★★★★☆</div><span class="btn">Add to Cart</span></div>
      <div class="product"><div class="photo" role="img" aria-label="Pump bottle of hand gel" style="background:linear-gradient(135deg,#ffffff,#9fd0ee)"></div><h4>Eyeglass Cleaner Bundle</h4><div class="price">$ 25.00 CAD</div><div class="stars">★★★★☆</div><span class="btn">Add to Cart</span></div>
      <div class="product"><div class="photo" role="img" aria-label="Three sanitizer bottles with blue caps" style="background:linear-gradient(135deg,#ffffff,#b8dcd0)"></div><h4>Detailing Kit</h4><div class="price">$ 25.00 CAD</div><div class="stars">★★★★☆</div><span class="btn">Add to Cart</span></div>
      <div class="product"><div class="photo" role="img" aria-label="Pink spray bottles on pale background" style="background:linear-gradient(135deg,#eef3f6,#e69ac0)"></div><h4>Microfibre Cloth – 10 Microfibres bundle</h4><div class="price">$ 25.00 CAD</div><div class="stars">★★★★☆</div><span class="btn">Add to Cart</span></div>
      <div class="product"><div class="photo" role="img" aria-label="Skincare tube on pink backdrop" style="background:linear-gradient(135deg,#f7b6c6,#f3d9de)"></div><h4>20 Pack Hand Sanitizer</h4><div class="price">$ 25.00 CAD</div><div class="stars">★★★★☆</div><span class="btn">Add to Cart</span></div>
      <div class="product"><div class="photo" role="img" aria-label="Set of white cosmetic bottles" style="background:linear-gradient(135deg,#f4f1ec,#d7d1c6)"></div><h4>Eyeglass Cleaner Bundle</h4><div class="price">$ 25.00 CAD</div><div class="stars">★★★★☆</div><span class="btn">Add to Cart</span></div>
      <div class="product"><div class="photo" role="img" aria-label="Green bottle with leaves on peach background" style="background:linear-gradient(135deg,#f2b48f,#7bb36a)"></div><h4>Detailing Kit</h4><div class="price">$ 25.00 CAD</div><div class="stars">★★★★☆</div><span class="btn">Add to Cart</span></div>
      <div class="product"><div class="photo" role="img" aria-label="Green pump bottles of hand soap" style="background:linear-gradient(135deg,#d8efc6,#3f9a3a)"></div><h4>Microfibre Cloth – 10 Microfibres bundle</h4><div class="price">$ 25.00 CAD</div><div class="stars">★★★★☆</div><span class="btn">Add to Cart</span></div>
    </div>
  </div>
</section>

<section class="blog">
  <div class="container">
    <h2 class="section-title">From the Blog</h2>
    <div class="blog-grid">
      <article class="post"><div class="photo" role="img" aria-label="Hands being washed under running water" style="background:linear-gradient(135deg,#d9dde0,#8f969c)"><div class="date">02<small>JUN</small></div></div><h4>Curabitur ligulasapien</h4><p>Vestibulum sagittis, nisi nec pellentesque suscipit, arcu mi maximus neque, vitae finibus ante odio ac lacus.</p></article>
      <article class="post"><div class="photo" role="img" aria-label="Close-up of bacteria under a microscope" style="background:linear-gradient(135deg,#5a8a94,#a9594c)"><div class="date">02<small>JUN</small></div></div><h4>Curabitur ligulasapien</h4><p>Vestibulum sagittis, nisi nec pellentesque suscipit, arcu mi maximus neque, vitae finibus ante odio ac lacus.</p></article>
      <article class="post"><div class="photo" role="img" aria-label="Person applying natural skincare" style="background:linear-gradient(135deg,#f3ede6,#c7d8e2)"><div class="date">02<small>JUN</small></div></div><h4>Curabitur ligulasapien</h4><p>Vestibulum sagittis, nisi nec pellentesque suscipit, arcu mi maximus neque, vitae finibus ante odio ac lacus.</p></article>
    </div>
    <span class="btn">View All</span>
  </div>
</section>

<section class="newsletter">
  <div class="container">
    <h3>Sign up for our Newsletter !</h3>
    <div class="field">Email Address</div>
    <div class="submit">Submit</div>
  </div>
</section>

<footer class="footer">
  <div class="container">
    <div class="footer-col"><h5>Main Links</h5><ul><li>All Products</li><li>About Us</li><li>Videos</li><li>Latest Blog</li></ul></div>
    <div class="footer-col"><h5>Information</h5><ul><li>Shipping Deals</li><li>Returns and Refunds</li><li>My Orders</li><li>Offers and Discounts</li></ul></div>
    <div class="footer-col"><h5>Support</h5><ul><li>Help &amp; Support</li><li>FAQ</li><li>Contact Us</li><li>Terms and Conditions</li></ul></div>
    <div class="footer-col"><h5>Contact Info</h5><ul>
      <li class="contact"><svg width="11" height="11" viewBox="0 0 12 12"><path d="M2 1h3l1 3-2 1c1 2 2 3 3 3l1-2 3 1v3c-6 0-9-3-9-9z" fill="#6ab43e"/></svg>4035550187</li>
      <li class="contact"><svg width="11" height="11" viewBox="0 0 12 12"><rect x="1" y="2.5" width="10" height="7" fill="none" stroke="#6ab43e" stroke-width="1.2"/><path d="M1 3l5 4 5-4" fill="none" stroke="#6ab43e" stroke-width="1.2"/></svg>brightleafnorthern@mailbox-example.com</li>
      <li class="contact"><svg width="11" height="11" viewBox="0 0 12 12"><circle cx="6" cy="6" r="5" fill="none" stroke="#6ab43e" stroke-width="1.2"/><path d="M1 6h10M6 1c2 3 2 7 0 10M6 1c-2 3-2 7 0 10" fill="none" stroke="#6ab43e" stroke-width="1"/></svg>www.socialpage-example.com/brightleafnorthern</li>
    </ul></div>
  </div>
</footer>
<div class="footer-bottom">brightleafnorthern © 2020. All Rights Reserved.</div>

</body>
</html>
```